Oven Cleaning Business owner needs business card design

Hi there,
Would like for a business card to be designed for myself, the owner of a professional oven cleaning business on the Sunshine Coast.
Would like it to look sleek, and modern-ish. Bit creative is encouraged too.
Include following:
Name/title: Corin ter Haghe, Owner
Phone number: 1300 482 916
Email: info@hearthshinecrew.com.au
Website: www.hearthshinecrew.com.au

```html
<!DOCTYPE html>
<html lang="en">
<head>
<meta charset="UTF-8">
<title>Hearthshine Crew – Business Card</title>
<link rel="stylesheet" href="https://fonts.googleapis.com/css2?family=Exo+2:wght@400;600;800&display=swap">
<style>
  :root {
    --teal: #4db6c1;
    --teal-deep: #3a9fab;
    --ink: #111416;
    --card-light: #f7f7f7;
    --card-shade: #dcdcdc;
    --backdrop: #1e1f20;
  }
  * { box-sizing: border-box; margin: 0; padding: 0; }
  html, body {
    width: 1200px; height: 900px; overflow: hidden;
    background: var(--backdrop);
    font-family: "Exo 2", sans-serif;
  }
  .stage {
    width: 1200px; height: 900px;
    display: flex; flex-direction: column; align-items: center; justify-content: center;
    gap: 40px;
  }
  .card {
    position: relative;
    width: 700px; height: 400px;
    background: linear-gradient(135deg, var(--card-shade) 0%, var(--card-light) 70%, #ffffff 100%);
    overflow: hidden;
  }

  /* front */
  .card-front .accent-band {
    position: absolute; left: 0; bottom: 0;
    width: 330px; height: 14px;
    background: var(--teal);
    clip-path: polygon(0 0, 100% 0, 96% 100%, 0 100%);
  }
  .identity {
    position: absolute; left: 48px; top: 138px;
  }
  .identity .person-name {
    font-size: 27px; font-weight: 400; letter-spacing: 0.5px;
    text-transform: uppercase; color: var(--teal); line-height: 1;
  }
  .identity .person-role {
    margin-top: 6px; font-size: 17px; color: var(--ink);
  }
  .divider {
    position: absolute; left: 48px; top: 222px;
    width: 560px; height: 1px; background: var(--teal);
  }
  .contact-list {
    position: absolute; left: 48px; top: 240px;
    list-style: none;
  }
  .contact-list li {
    display: flex; align-items: center; gap: 10px;
    font-size: 17px; color: var(--ink); line-height: 27px;
  }
  .contact-list svg { width: 15px; height: 15px; flex: none; }
  .website {
    position: absolute; right: 92px; bottom: 56px;
    font-size: 20px; color: var(--ink);
  }
  .website .domain { color: var(--teal); }

  .brand {
    display: flex; align-items: center; gap: 14px;
  }
  .brand .brand-dot {
    width: 46px; height: 46px; border-radius: 50%;
    background: var(--teal); flex: none;
  }
  .brand .brand-name {
    font-weight: 800; color: var(--ink); text-transform: uppercase;
    line-height: 0.95;
  }
  .card-front .brand {
    position: absolute; right: 48px; top: 110px;
  }
  .card-front .brand-name { font-size: 30px; }

  /* back */
  .card-back {
    display: flex; align-items: center; justify-content: center;
  }
  .card-back .brand { gap: 22px; }
  .card-back .brand-dot { width: 84px; height: 84px; }
  .card-back .brand-name { font-size: 54px; }
</style>
</head>
<body>
<main class="stage">
  <section class="card card-front">
    <div class="identity">
      <p class="person-name">Corin ter Haghe</p>
      <p class="person-role">Owner</p>
    </div>
    <div class="divider"></div>
    <ul class="contact-list">
      <li>
        <svg viewBox="0 0 16 16" aria-hidden="true"><path fill="#4db6c1" d="M3.6 1.2l2.2 2.6-1.3 1.6c.8 2 2.2 3.4 4.1 4.2l1.6-1.3 2.6 2.2-1.4 2.3C6.8 12.6 3.4 9.2 2.2 4.6z"/></svg>
        1300 482 916
      </li>
      <li>
        <svg viewBox="0 0 16 16" aria-hidden="true"><rect x="1" y="3.5" width="14" height="9" fill="#4db6c1"/><path d="M1 3.5l7 5 7-5" fill="none" stroke="#ffffff" stroke-width="1.2"/></svg>
        info@hearthshinecrew.com.au
      </li>
    </ul>
    <div class="brand">
      <span class="brand-dot"></span>
      <span class="brand-name">Hearthshine<br>Crew</span>
    </div>
    <p class="website">www.<span class="domain">hearthshinecrew</span>.com.au</p>
    <div class="accent-band"></div>
  </section>

  <section class="card card-back">
    <div class="brand">
      <span class="brand-dot"></span>
      <span class="brand-name">Hearthshine<br>Crew</span>
    </div>
  </section>
</main>
</body>
</html>
```